Oakleaf medical

We are a doctors surgery, providing medical services to all ages

we aim for a professional as well as an eye catching look for the signs that can be seen by passing vehicles and people who walk by

trustworthy quality medical care to to all patients, we treat like family

Name- Brookmere Oakleaf Medical practice

Target Market(s)

all ages, adults
the elderly

Industry/Entity Type

Medical

Requirements
Must have
• eye catching,
obvious medical service location

```html
<!DOCTYPE html>
<html lang="en">
<head>
<meta charset="UTF-8">
<title>Brookmere Oakleaf Medical Practice – Sign</title>
<link rel="stylesheet" href="https://fonts.googleapis.com/css2?family=Montserrat:wght@500;600&family=Sanchez&display=swap">
<style>
  :root {
    --stage: #2d333b;
    --sign-white: #ffffff;
    --sign-fade: #e4e7ea;
    --heading-grey: #4a4f54;
    --practice-pink: #ee62a8;
    --phone-blue: #1a6fb8;
    --band-green: #6cbf45;
    --ring-blue: #1e9ad6;
    --photo-light: #f3f5f8;
    --photo-mid: #d9c3b0;
    --photo-cool: #9fb7cf;
  }
  html, body {
    margin: 0;
    padding: 0;
    width: 1200px;
    height: 750px;
    overflow: hidden;
    background: var(--stage);
  }
  .sign {
    position: absolute;
    left: 100px;
    top: 241px;
    width: 1000px;
    height: 267px;
    overflow: hidden;
    background: linear-gradient(to bottom, var(--sign-white) 0%, var(--sign-white) 62%, var(--sign-fade) 100%);
    font-family: "Montserrat", Arial, sans-serif;
  }
  .photo-area {
    position: absolute;
    left: 620px;
    top: 0;
    width: 380px;
    height: 267px;
    z-index: 0;
    background:
      linear-gradient(to right, var(--sign-white) 0%, rgba(255,255,255,0) 20%),
      radial-gradient(ellipse at 30% 40%, var(--photo-mid) 0%, rgba(217,195,176,0) 45%),
      linear-gradient(to bottom, var(--photo-light) 0%, var(--photo-cool) 100%);
  }
  .brand-mark {
    position: absolute;
    left: 24px;
    top: 27px;
    width: 138px;
    height: 138px;
    z-index: 1;
    display: flex;
    align-items: center;
    justify-content: center;
  }
  .brand-mark svg {
    position: absolute;
    inset: 0;
  }
  .brand-name {
    position: relative;
    width: 100px;
    text-align: center;
    font-weight: 600;
    font-size: 17px;
    line-height: 1.15;
    color: var(--phone-blue);
  }
  .title-block {
    position: absolute;
    left: 208px;
    top: 36px;
    width: 410px;
    z-index: 1;
    text-align: center;
  }
  .practice-owner {
    margin: 0;
    font-weight: 500;
    font-size: 30px;
    letter-spacing: 1px;
    color: var(--heading-grey);
    line-height: 36px;
    white-space: nowrap;
  }
  .practice-type {
    margin: 0;
    font-weight: 500;
    font-size: 49px;
    color: var(--practice-pink);
    line-height: 60px;
    white-space: nowrap;
  }
  .phone {
    position: absolute;
    left: 233px;
    top: 135px;
    z-index: 1;
    display: flex;
    align-items: center;
    gap: 12px;
    font-weight: 500;
    font-size: 48px;
    color: var(--phone-blue);
    line-height: 56px;
    white-space: nowrap;
  }
  .tagline-band {
    position: absolute;
    left: 0;
    top: 224px;
    width: 640px;
    height: 33px;
    z-index: 1;
    background: linear-gradient(to right, var(--band-green) 88%, rgba(108,191,69,0) 100%);
  }
  .tagline {
    position: absolute;
    left: 86px;
    top: 0;
    margin: 0;
    font-family: "Sanchez", Georgia, serif;
    font-size: 22px;
    line-height: 33px;
    color: var(--sign-white);
    white-space: nowrap;
  }
</style>
</head>
<body>
  <section class="sign">
    <div class="photo-area" role="img" aria-label="Photo of a smiling doctor with a stethoscope in front of a family with a child greeting another doctor"></div>

    <div class="brand-mark">
      <svg width="138" height="138" viewBox="0 0 138 138" aria-hidden="true">
        <circle cx="69" cy="69" r="66" fill="none" stroke="var(--ring-blue)" stroke-width="5"/>
      </svg>
      <span class="brand-name">Oakleaf medical</span>
    </div>

    <div class="title-block">
      <h1 class="practice-owner">BROOKMERE OAKLEAF</h1>
      <p class="practice-type">Medical Practice</p>
    </div>

    <div class="phone">
      <svg width="32" height="32" viewBox="0 0 24 24" aria-hidden="true">
        <path fill="var(--band-green)" d="M6.6 10.8c1.4 2.8 3.8 5.1 6.6 6.6l2.2-2.2c.3-.3.7-.4 1-.2 1.1.4 2.3.6 3.6.6.6 0 1 .4 1 1V20c0 .6-.4 1-1 1C10.6 21 3 13.4 3 4c0-.6.4-1 1-1h3.5c.6 0 1 .4 1 1 0 1.3.2 2.5.6 3.6.1.3 0 .7-.2 1L6.6 10.8z"/>
      </svg>
      <span class="phone-number">222 555 0148</span>
    </div>

    <div class="tagline-band">
      <p class="tagline">Trustworthy Medical Care for all Patients</p>
    </div>
  </section>
</body>
</html>
```